Fernhollow Glow Clinic is a rebranding of fernhollowfootcare.com.au. The business provides Medical Injectables (botox and fillers) Laser and IPL therapies, Podiatry and remedial massage. We have a logo already done (yay! sketch hive!) you can download it here: http://fernhollowglowclinic.com/brand_assets.zip . We are after a clean, long scrolling website (in the style of quvaret.com). There will be 6 subpages (or sections depending on how you create it) (1) Cosmetic Injections (2) Podiatry (3) Remedial Massage (4) Laser Therapies (5) Skin Care (6) Customer Club and Special Offers. The target demographic is wealthy or aspirational women 35+.

Font styles to use
Sans Serif

Colors
9bcb3c
33a6d7

Requirements
Must have
• Simple, clean long scroller like quvaret.com
Nice to have
• Congruence with existing corporate identity.

```html
<!DOCTYPE html>
<html lang="en">
<head>
<meta charset="utf-8">
<title>Fernhollow Glow Clinic</title>
<link href="https://fonts.googleapis.com/css2?family=Open+Sans:wght@400;600;700&family=Titillium+Web:wght@400;600;700&display=swap" rel="stylesheet">
<style>
:root{
  --blue:#1b8fd6;
  --blue-deep:#0a86cf;
  --green:#9bcb3c;
  --green-dark:#8cbf2c;
  --sky:#33a6d7;
  --ink:#3b3b3b;
  --muted:#6d6d6d;
  --grey-band:#efefef;
  --footer:#1c1f2a;
  --white:#ffffff;
}
*{margin:0;padding:0;box-sizing:border-box}
html,body{width:1200px;height:3051px;overflow:hidden;background:var(--white)}
body{position:relative;font-family:"Open Sans",Arial,sans-serif;color:var(--ink)}
.abs{position:absolute}
h1,h2,h3{font-family:"Titillium Web",Arial,sans-serif;font-weight:600}
p.copy{font-size:12.5px;line-height:24.4px;color:#4a4a4a}

.top-rule{left:0;top:0;width:1200px;height:6px;background:var(--blue)}
.brand{left:98px;top:34px;display:flex;align-items:center;gap:12px}
.brand-dot{width:26px;height:26px;border-radius:50%;background:var(--green)}
.brand-name{font-family:"Titillium Web",sans-serif;font-size:28px;font-weight:400;color:#4d6b8a;letter-spacing:1px}

.nav{left:0;top:134px;width:1200px;height:69px;background:var(--blue)}
.nav-accent{left:0;top:203px;width:1200px;height:6px;background:var(--green)}
.nav ul{list-style:none;display:flex;height:100%;padding-left:100px}
.nav li{height:100%;display:flex;align-items:center;justify-content:center;color:var(--white);font-size:14px}
.nav li.active{background:var(--green);width:140px}
.nav li.i2{width:180px}.nav li.i3{width:130px}.nav li.i4{width:180px}.nav li.i5{width:130px}.nav li.i6{width:220px}

.hero{left:0;top:209px;width:1200px;height:517px;background:linear-gradient(100deg,#efe1d4 0%,#d9b99d 35%,#e6cdb6 60%,#f3ebe3 100%)}
.hero-arrow{top:440px;width:32px;height:32px;border-radius:50%;background:rgba(255,255,255,.9);display:flex;align-items:center;justify-content:center}
.dots{left:572px;top:697px;display:flex;gap:5px}
.dots span{width:11px;height:11px;border-radius:50%;border:2px solid #fff;background:#ddd}
.dots span.on{background:var(--blue)}

.welcome{left:100px;top:752px;width:1000px;text-align:center}
.welcome h1{font-size:30px;color:var(--green);margin-bottom:6px}
.welcome h1 span{color:var(--blue)}

.band-grey{left:0;top:936px;width:1200px;height:335px;background:linear-gradient(120deg,#f6f6f6,#e9e9e9 50%,#f4f4f4)}
.band-blue{left:0;top:1607px;width:1200px;height:335px;background:var(--sky)}
.band-dark{left:0;top:2272px;width:1200px;height:271px;background:linear-gradient(90deg,#3a2c22,#6b5a4c 50%,#3b2d23)}

.photo{box-shadow:0 8px 10px -6px rgba(0,0,0,.45)}
.service h2{font-size:28px;color:var(--green);margin-bottom:4px}
.service.on-blue h2{color:var(--white)}
.service.on-blue p.copy{color:var(--white)}
.btn{display:inline-flex;align-items:center;justify-content:center;width:124px;height:51px;border-radius:6px;color:#fff;font-size:12px;margin-top:22px}
.btn.blue{background:var(--blue-deep)}
.btn.green{background:var(--green)}

.skin{left:100px;top:2310px;width:1000px;text-align:center;color:#fff}
.skin h2{font-size:30px;margin-bottom:4px}
.skin p.copy{color:#fff}

.club h2{font-size:30px;color:var(--green)}
.post-date{font-size:11px;color:#555}
.post-title{font-size:12.5px;font-weight:700;color:#222;margin-top:6px}
.offer{left:791px;top:2565px;width:309px;height:287px;background:linear-gradient(160deg,#b99a78,#e7cbb0 55%,#c8a584)}
.offer h3{position:absolute;left:0;top:90px;width:100%;text-align:center;font-size:27px;font-weight:700;color:#fff;text-shadow:0 2px 3px rgba(0,0,0,.35)}
.offer .btn{position:absolute;left:98px;top:146px;width:124px;height:34px;margin:0;border-radius:3px;font-size:11px}

.foot-rule{left:0;top:2888px;width:1200px;height:8px;background:var(--blue)}
.footer{left:0;top:2896px;width:1200px;height:155px;background:var(--footer);color:#e8e8e8;font-size:13px}
.footer .copyright{position:absolute;left:100px;top:48px}
.footer .links{position:absolute;left:100px;top:84px}
.social{position:absolute;left:956px;top:62px;display:flex;gap:12px}
.social span{width:30px;height:30px;border-radius:5px;background:var(--sky)}
</style>
</head>
<body>
<div class="abs top-rule"></div>
<div class="abs brand"><span class="brand-dot"></span><span class="brand-name">FERNHOLLOW GLOW CLINIC</span></div>

<nav class="abs nav">
  <ul>
    <li class="active">Home</li><li class="i2">About Us</li><li class="i3">Services</li><li class="i4">Packages</li><li class="i5">Gift Vouchers</li><li class="i6">Contact Us</li>
  </ul>
</nav>
<div class="abs nav-accent"></div>

<div class="abs hero" role="img" aria-label="Couple relaxing during a shoulder massage at the spa"></div>
<div class="abs hero-arrow" style="left:38px"><svg width="12" height="12" viewBox="0 0 12 12"><path d="M8 1 3 6l5 5" stroke="#333" stroke-width="2" fill="none"/></svg></div>
<div class="abs hero-arrow" style="left:1140px"><svg width="12" height="12" viewBox="0 0 12 12"><path d="M4 1l5 5-5 5" stroke="#333" stroke-width="2" fill="none"/></svg></div>
<div class="abs dots"><span class="on"></span><span></span><span></span></div>

<section class="abs welcome">
  <h1>Welcome To <span>Fernhollow Glow</span></h1>
  <p class="copy">Lorem ipsum dolor sit amet, consectetuer adipiscing elit, sed diam nonummy nibh euismod tincidunt ut laoreet dolore magna aliquam erat volutpat. Ut wisi enim ad minim veniam, quis nostrud exerci tation ullamcorper suscipit lobortis nisl ut aliquip ex ea commodo consequat. Lorem ipsum dolor sit amet, consectetuer adipiscing elit, sed diam nonummy nibh euismod tincidunt ut laoreet dolore magna aliquam erat volutpat. Ut wisi enim ad minim veniam, quis nostrud exerci tation ullamcorper suscipit lobortis nisl ut aliquip ex ea commodo consequat.</p>
</section>

<div class="abs band-grey"></div>
<div class="abs photo" style="left:100px;top:970px;width:402px;height:259px;background:linear-gradient(110deg,#c9d3d8,#e8c3a6 50%,#d9cfc6)" role="img" aria-label="Client receiving a cosmetic injection"></div>
<section class="abs service" style="left:523px;top:975px;width:560px">
  <h2>Cosmetic Injections</h2>
  <p class="copy">Lorem ipsum dolor sit amet, consectetuer adipiscing elit, sed diam nonummy nibh euismod tincidunt ut laoreet dolore magna aliquam erat volutpat. Ut wisi enim ad minim veniam, quis nostrud exerci tation ullamcorper suscipit lobortis nisl ut aliquip ex ea commodo consequat. Lorem ipsum dolor sit amet, consectetuer adipiscing elit, sed diam nonummy nibh euismod tincidunt ut laoreet dolore magna</p>
  <span class="btn blue" style="margin-left:6px">Read more</span>
</section>

<section class="abs service" style="left:100px;top:1310px;width:560px">
  <h2>Podiatry</h2>
  <p class="copy">Lorem ipsum dolor sit amet, consectetuer adipiscing elit, sed diam nonummy nibh euismod tincidunt ut laoreet dolore magna aliquam erat volutpat. Ut wisi enim ad minim veniam, quis nostrud exerci tation ullamcorper suscipit lobortis nisl ut aliquip ex ea commodo consequat. Lorem ipsum dolor sit amet, consectetuer adipiscing elit, sed diam nonummy nibh euismod tincidunt ut laoreet dolore magna</p>
  <span class="btn blue">Read more</span>
</section>
<div class="abs photo" style="left:696px;top:1304px;width:404px;height:260px;background:linear-gradient(120deg,#8f8f8f,#d7b39a 45%,#e6c7b0 70%,#a9a9a9)" role="img" aria-label="Hands massaging a foot during podiatry care"></div>

<div class="abs band-blue"></div>
<div class="abs photo" style="left:100px;top:1643px;width:402px;height:259px;background:linear-gradient(100deg,#f3f0ec,#d7a888 45%,#c99775 65%,#efe9e3)" role="img" aria-label="Woman receiving a remedial back massage"></div>
<section class="abs service on-blue" style="left:523px;top:1650px;width:560px">
  <h2>Remedial Massage</h2>
  <p class="copy">Lorem ipsum dolor sit amet, consectetuer adipiscing elit, sed diam nonummy nibh euismod tincidunt ut laoreet dolore magna aliquam erat volutpat. Ut wisi enim ad minim veniam, quis nostrud exerci tation ullamcorper suscipit lobortis nisl ut aliquip ex ea commodo consequat. Lorem ipsum dolor sit amet, consectetuer adipiscing elit, sed diam nonummy nibh euismod tincidunt ut laoreet dolore magna</p>
  <span class="btn green" style="margin-left:6px">Read more</span>
</section>

<section class="abs service" style="left:100px;top:1983px;width:560px">
  <h2>Laser Therapies</h2>
  <p class="copy">Lorem ipsum dolor sit amet, consectetuer adipiscing elit, sed diam nonummy nibh euismod tincidunt ut laoreet dolore magna aliquam erat volutpat. Ut wisi enim ad minim veniam, quis nostrud exerci tation ullamcorper suscipit lobortis nisl ut aliquip ex ea commodo consequat. Lorem ipsum dolor sit amet, consectetuer adipiscing elit, sed diam nonummy nibh euismod tincidunt ut laoreet dolore magna</p>
  <span class="btn blue">Read more</span>
</section>
<div class="abs photo" style="left:696px;top:1979px;width:404px;height:258px;background:linear-gradient(120deg,#8f8f8f,#d7b39a 45%,#e6c7b0 70%,#a9a9a9)" role="img" aria-label="Treatment of the lower leg during laser therapy"></div>

<div class="abs band-dark" role="img" aria-label="Soft-focus spa interior behind the skin care section"></div>
<section class="abs skin">
  <h2>Skin Care</h2>
  <p class="copy">Lorem ipsum dolor sit amet, consectetuer adipiscing elit, sed diam nonummy nibh euismod tincidunt ut laoreet dolore magna aliquam erat volutpat. Ut wisi enim ad minim veniam, quis nostrud exerci tation ullamcorper suscipit lobortis nisl ut aliquip ex ea commodo consequat. Lorem ipsum dolor sit amet, consectetuer adipiscing elit, sed diam nonummy nibh euismod tincidunt ut laoreet dolore magna</p>
  <span class="btn green" style="margin-top:18px">Read more</span>
</section>

<section class="abs club" style="left:100px;top:2572px;width:660px">
  <h2>Customer Club</h2>
</section>
<div class="abs" style="left:100px;top:2636px;width:319px;height:151px;background:linear-gradient(100deg,#2a1d16,#c8927a 55%,#e7a9b8)" role="img" aria-label="Woman relaxing with flowers during a spa treatment"></div>
<div class="abs" style="left:437px;top:2636px;width:320px;height:151px;background:linear-gradient(100deg,#5f8a4a,#d7b197 50%,#b98a70)" role="img" aria-label="Woman resting with a flower in her hair"></div>
<div class="abs" style="left:100px;top:2801px"><div class="post-date">Aug 9, 2013 &nbsp;3 comments</div><div class="post-title">Lorem ipsum dolor sit amet</div></div>
<div class="abs" style="left:437px;top:2801px"><div class="post-date">Aug 9, 2013 &nbsp;3 comments</div><div class="post-title">Lorem ipsum dolor sit amet</div></div>

<div class="abs offer" role="img" aria-label="Relaxed client with a towel wrapped around her hair">
  <h3>Speical Offers</h3>
  <span class="btn green">READ MORE</span>
</div>

<div class="abs foot-rule"></div>
<footer class="abs footer">
  <div class="copyright">Copyright © 2014 Fernhollow Glow Clinic. All Rights Reserved.</div>
  <div class="links">Privacy Policy | Site Map | Site by Lumenworks</div>
  <div class="social"><span></span><span></span><span></span><span></span></div>
</footer>
</body>
</html>
```